Institutional website for an IT Consulting company

Web design + HTML + CSS / Bootstrap + JS (interaction) integration in order to extend our existing website brightvale.coop.
Our website is currently aiming only for recruitment and not for customers, we want to provide a fluid transition between customer side website (this project) and recruitment website (existing site).

Ideally we would love the new design to be "inspired" by our actual graphic chart (Colors mainly). It should provide a great user experience and a landing page (or any mean) allowing the visitor to easily switch from the end customer front end (this project), the recruitment front end (existing front end https://www.brightvale.coop/) and the existing member front end (an other existing front end dedicated to members already existing).

In attachment you will find the expected site content mainly a one page with a first level of information and "link" to sub pages (a way to directly access this sub pages should also be provided).

The website should be accessible on mobile device and desktop.

The attachment is in french as it reflect the final site content, but if google translate isn't sufficient to have a general idea of the content, feel free to ask. We would love to have some visual representation for some categories.

Target Market(s)

fortune 500 companies

Industry/Entity Type

It Company

Coding

Coded - Design and coding required

Number of Pages Required

5+ page

Requirements
Must have
• This project must have an easy way to navigate between 3 sub sites, the customer one (the one designed here), the consultant / recruitment one (the existing one at brightvale.coop), the members one.

A one page experience at first leading to detail pages.

Custom made visuals to illustrate each categories.

Inspiration websites : quorb[.]fr ; tasknest[.]com ; dovrally[.] com ...

Be inspired by the existing color from our logo and existing website at brightvale[.]coop

```html
<!DOCTYPE html>
<html lang="en">
<head>
<meta charset="utf-8">
<title>Brightvale.coop — IT Consulting Cooperative</title>
<link href="https://fonts.googleapis.com/css2?family=Oswald:wght@500&family=Montserrat:ital,wght@0,400;0,500;0,600;0,700;1,400&display=swap" rel="stylesheet">
<style>
:root{
  --teal:#14adb3;
  --teal-dark:#0b4540;
  --teal-deep:#0e4a44;
  --purple:#3c2a5e;
  --ink:#1a1a1a;
  --text:#333;
  --muted:#555;
  --footer:#0e1719;
  --line:#d5d5d5;
  --white:#fff;
}
*{margin:0;padding:0;box-sizing:border-box}
html,body{width:1200px;height:4138px;overflow:hidden}
body{position:relative;font-family:"Montserrat",sans-serif;color:var(--text);background:var(--white)}
.abs{position:absolute}
.heading{font-family:"Oswald",sans-serif;font-weight:500;color:var(--ink);letter-spacing:.5px}
.btn{position:absolute;display:flex;align-items:center;justify-content:center;font-weight:700;font-size:13px;letter-spacing:.5px;color:var(--white);text-transform:uppercase}

/* header */
.site-header{position:absolute;left:0;top:0;width:1200px;height:77px;background:var(--white)}
.brand{position:absolute;left:128px;top:18px;font-weight:700;font-size:30px;color:var(--teal-dark);letter-spacing:-.5px}
.nav{position:absolute;top:28px;left:468px;display:flex;gap:29px;font-size:13px;color:var(--ink)}
.login{left:983px;top:19px;width:93px;height:34px;background:var(--teal-dark);font-weight:500;font-size:12px}

/* hero */
.hero{position:absolute;left:0;top:77px;width:1200px;height:524px;background:linear-gradient(110deg,#7a5a3c 0%,#4a3a30 35%,#2b2623 65%,#1d1b1a 100%)}
.hero-title{position:absolute;left:0;width:1200px;top:140px;text-align:center;font-family:"Oswald",sans-serif;font-weight:500;font-size:64px;color:var(--white)}
.search{position:absolute;left:214px;top:236px;width:772px;height:63px;background:var(--white);border:3px solid var(--white);display:flex}
.search-field{display:flex;align-items:center;gap:14px;padding-left:16px;font-size:13px;color:#666}
.search-skills{width:340px;border-right:1px solid #ddd}
.search-city{width:285px}
.search-btn{flex:1;background:var(--teal-dark);color:var(--white);display:flex;align-items:center;justify-content:center;gap:8px;font-weight:700;font-size:14px}
.btn-member{left:419px;top:323px;width:148px;height:50px;background:var(--teal);font-weight:500;text-transform:none;font-size:13px}
.btn-join{left:575px;top:323px;width:206px;height:50px;border:2px solid var(--white);font-weight:500;text-transform:none;font-size:13px}
.accent-bars .bar1{left:151px;top:575px;width:5px;height:101px;background:var(--teal)}
.accent-bars .bar2{left:165px;top:575px;width:4px;height:72px;background:var(--teal-dark)}

/* service provider */
.sp-title{left:148px;top:740px;font-size:56px}
.sp-text{left:149px;top:836px;width:470px;font-size:16px;line-height:27px;color:var(--ink)}
.sp-text strong{color:var(--teal-dark);font-weight:600}
.btn-contact{left:149px;top:914px;width:172px;height:47px;background:var(--teal-dark);font-size:12px}
.btn-video{left:333px;top:914px;width:173px;height:47px;background:var(--teal);font-size:12px}
.video{left:720px;top:747px;width:404px;height:236px;background:linear-gradient(180deg,#f4f4f2,#e6ebe9);border-bottom:4px solid #111;overflow:hidden}
.video-bar{position:absolute;left:0;top:0;width:100%;height:38px;background:linear-gradient(180deg,rgba(0,0,0,.55),rgba(0,0,0,0));color:var(--white);font-size:12px;display:flex;align-items:center;gap:8px;padding-left:10px}
.video-bar i{display:block;width:24px;height:24px;border-radius:50%;background:var(--white)}
.play{position:absolute;left:177px;top:100px;width:52px;height:36px;border-radius:8px;background:#222;display:flex;align-items:center;justify-content:center}

/* AEC-COPA */
.copa{position:absolute;left:0;top:1115px;width:1200px;height:684px;background:var(--purple)}
.copa-art{left:32px;top:90px;width:530px;height:449px;border-radius:8px;background:radial-gradient(circle at 55% 45%,#7f5fd6 0%,#5a3f9a 30%,rgba(60,42,94,0) 70%)}
.copa-title{left:618px;top:70px;font-size:50px;color:var(--white)}
.copa-body{left:618px;top:170px;width:500px;font-size:14px;line-height:22.5px;color:#f1eef7}
.copa-body p{margin-bottom:22px}

/* CAE-Scop */
.cae-title{left:0;top:1860px;width:1200px;text-align:center;font-size:52px}
.feature{position:absolute;top:1983px;width:300px;text-align:center}
.feature-art{width:150px;height:134px;margin:0 auto;border-radius:6px;background:linear-gradient(135deg,#d9f2f4,#f3e3f7)}
.feature h3{margin-top:28px;font-size:18px;font-weight:600;color:var(--ink)}
.feature p{margin:14px auto 0;width:280px;font-size:12px;line-height:19px;color:var(--text)}
.feature .btn{position:static;margin:24px auto 0;width:117px;height:32px;background:var(--teal);font-size:12px;text-transform:none}

/* testimonial */
.testimonial{position:absolute;left:0;top:2391px;width:1200px;height:476px;background:linear-gradient(90deg,#0d4540,#0f4f49 60%,#124f4a)}
.t-block{left:119px;top:161px;width:141px;height:257px;background:var(--teal)}
.t-photo{left:149px;top:85px;width:285px;height:304px;background:linear-gradient(160deg,#cfd7d0,#9aa79e)}
.t-quote{left:500px;top:64px;width:544px;text-align:center}
.t-quote p{margin-top:36px;font-style:italic;font-size:20px;line-height:30px;color:#e8f3f1}
.t-name{margin-top:26px;font-weight:700;font-size:17px;color:var(--white)}
.t-role{margin-top:6px;font-size:13px;color:#d7e8e6;letter-spacing:.5px}

/* blog */
.blog-title{left:0;top:2925px;width:1200px;text-align:center;font-size:52px}
.post{position:absolute;top:3037px;width:285px}
.post-img{position:relative;height:204px;background:linear-gradient(135deg,#8a8f92,#3c4246)}
.post-date{position:absolute;right:14px;bottom:-14px;width:73px;height:64px;background:var(--teal);color:var(--white);text-align:center;padding-top:6px}
.post-date b{display:block;font-size:28px;line-height:30px;font-weight:600}
.post-date span{font-size:11px}
.post h4{margin-top:22px;font-size:15px;line-height:22px;font-weight:700;color:var(--ink)}
.post p{margin-top:14px;font-size:12px;line-height:22px;color:var(--muted)}
.post svg{margin-top:16px;display:block}

/* contact */
.contact-band{position:absolute;left:0;top:3748px;width:1200px;height:390px;background:var(--footer)}
.contact-card{left:172px;top:3508px;width:856px;height:478px;background:var(--white)}
.enquiry-title{left:37px;top:56px;font-size:26px;letter-spacing:1px}
.field{position:absolute;left:37px;width:386px;border-bottom:1px solid var(--line);font-size:12px;color:#666;padding-bottom:8px}
.btn-send{left:37px;top:379px;width:165px;height:42px;background:var(--teal-dark);font-size:12px}
.info{left:490px;top:0;width:366px;height:478px;background:var(--teal)}
.info-title{left:46px;top:56px;font-size:26px;color:var(--white);letter-spacing:1px}
.info-item{position:absolute;left:38px;display:flex;gap:14px;color:var(--white)}
.info-item small{display:block;font-size:11px;letter-spacing:2px;text-transform:uppercase;color:#e3f7f8}
.info-item b{display:block;font-size:15px;line-height:23px;font-weight:700}
.btn-map{left:45px;top:380px;width:178px;height:41px;border:2px solid var(--white);font-size:12px}
.social{left:0;top:4030px;width:1200px;display:flex;justify-content:center;gap:22px}
.social i{display:block;width:14px;height:14px;border-radius:50%;background:var(--white)}
.copyright{left:0;top:4068px;width:1200px;text-align:center;font-size:12px;color:#e6e6e6}
</style>
</head>
<body>

<header class="site-header">
  <div class="brand">BRIGHTVALE.COOP</div>
  <nav class="nav"><span>Home</span><span>Service Provider</span><span>CAE-Scop</span><span>Experts</span><span>News</span><span>Contact Us</span></nav>
  <div class="btn login">LOGIN</div>
</header>

<section class="hero" role="img" aria-label="Photo of two smiling colleagues working on a laptop">
  <h1 class="hero-title">We Accelerate Your Success</h1>
  <div class="search">
    <div class="search-field search-skills">
      <svg width="20" height="20" viewBox="0 0 20 20"><circle cx="8" cy="8" r="6" fill="none" stroke="#14adb3" stroke-width="2.5"/><path d="M12.5 12.5l5 5" stroke="#14adb3" stroke-width="2.5"/></svg>
      Looking for skills
    </div>
    <div class="search-field search-city">
      <svg width="14" height="20" viewBox="0 0 14 20"><path d="M7 1a6 6 0 0 0-6 6c0 5 6 12 6 12s6-7 6-12a6 6 0 0 0-6-6z" fill="#14adb3"/><circle cx="7" cy="7" r="2.2" fill="#fff"/></svg>
      Search for City or Zip Code
    </div>
    <div class="search-btn">
      <svg width="18" height="18" viewBox="0 0 20 20"><circle cx="8" cy="8" r="6" fill="none" stroke="#14adb3" stroke-width="2.5"/><path d="M12.5 12.5l5 5" stroke="#14adb3" stroke-width="2.5"/></svg>
      SEARCH
    </div>
  </div>
  <div class="btn btn-member">I am Brightvale</div>
  <div class="btn btn-join">I want to join Brightvale</div>
</section>

<div class="accent-bars"><div class="abs bar1"></div><div class="abs bar2"></div></div>

<section class="service-provider">
  <h2 class="abs heading sp-title">Service Provider</h2>
  <p class="abs sp-text"><strong>BRIGHTVALE.COOP</strong> is a cooperative and participatory company specializing in digital services.</p>
  <div class="btn btn-contact">Contactez-nous</div>
  <div class="btn btn-video">Voir la video</div>
  <div class="abs video" role="img" aria-label="Video thumbnail with a hand-drawn illustration of characters and houses">
    <div class="video-bar"><i></i>BRIGHTVALE.COOP</div>
    <div class="play"><svg width="14" height="16" viewBox="0 0 14 16"><path d="M0 0l14 8-14 8z" fill="#fff"/></svg></div>
  </div>
</section>

<section class="copa">
  <div class="abs copa-art" role="img" aria-label="Isometric illustration of a laptop with floating charts and graphs"></div>
  <h2 class="abs heading copa-title">What is a AEC-COPA?</h2>
  <div class="abs copa-body">
    <p>Brightvale is an activity and employment cooperative which has the legal status of a cooperative and participatory association (SCOP in French). Do these words seem fuzzy to you? Here is an explanation that will allow you to understand how we operate:</p>
    <p>An AEC like Brightvale gathers a group of consultant who wish to develop their own entrepreneur activity whilst being part of a collective company and benefiting from the salaried status.</p>
    <p>We chose the legal status of COPA so that each of our S/E can work on their professional activity whilst having the opportunity to profit from the contributors' experiences in their area. Because of this status, we adopted a democratic governance: all decision-making are taken by vote of the associated S/E. The S/E can become associated by simple request and have an obligation to become one after 3 years of service.</p>
    <p>Regarding the stewardship, it is a volunteer work that lasts for only 3 years and is available to all our S/E and has to be voted by all the S/E.</p>
  </div>
</section>

<section class="cae">
  <h2 class="abs heading cae-title">Brightvale CAE-Scop</h2>
  <div class="feature" style="left:141px">
    <div class="feature-art" role="img" aria-label="Illustration of people around a target"></div>
    <h3>Custom-made S/E</h3>
    <p>Accordingly to your needs, our consultant will be able to assist you in achieving your projects</p>
    <div class="btn">Find out more</div>
  </div>
  <div class="feature" style="left:449px">
    <div class="feature-art" role="img" aria-label="Illustration of people assembling puzzle pieces"></div>
    <h3>A team at your service</h3>
    <p>Brightvale as a AEC-COPA offers you a service, not from an independent to a customer perspective but from a community to a customer.</p>
    <div class="btn">Find out more</div>
  </div>
  <div class="feature" style="left:757px">
    <div class="feature-art" style="width:230px" role="img" aria-label="Illustration of people with coins and a phone payment screen"></div>
    <h3>A Fair Pay</h3>
    <p>At Brightvale, the S/E gain directly what they work for.</p>
    <div class="btn">Find out more</div>
  </div>
</section>

<section class="testimonial">
  <div class="abs t-block"></div>
  <div class="abs t-photo" role="img" aria-label="Portrait photo of the marketing head"></div>
  <div class="abs t-quote">
    <svg width="52" height="42" viewBox="0 0 52 42"><path d="M0 20C0 8 6 1 18 0v7c-6 1-9 5-9 11h9v24H0zM29 20C29 8 35 1 47 0v7c-6 1-9 5-9 11h9v24H29z" fill="#14adb3"/></svg>
    <p>Lorem Ipsum is simply dummy text of the printing and typesetting industry. Lorem Ipsum has been the industry's standard dummy text ever since the 1500s, when an unknown printer took a galley of type and scrambled it to make a type specimen book. It has survived not only five centuries, but also the leap into electronic typesetting, remaining essentially unchanged.</p>
    <div class="t-name">MARCEL DORWIN</div>
    <div class="t-role">Marketing head</div>
  </div>
</section>

<section class="blog">
  <h2 class="abs heading blog-title">Latest Blog</h2>
  <article class="post" style="left:149px">
    <div class="post-img" role="img" aria-label="Photo of a desk with keyboard, headphones and tablet from above"><div class="post-date"><b>25</b><span>Jul, 2020</span></div></div>
    <h4>Lorem Ipsum is simply dummy text of the printing</h4>
    <p>Lorem Ipsum is simply dummy text of the printing and typesetting industry. Lorem Ipsum has been the industry's.</p>
    <svg width="30" height="14" viewBox="0 0 30 14"><path d="M0 7h28M22 1l6 6-6 6" fill="none" stroke="#222" stroke-width="2"/></svg>
  </article>
  <article class="post" style="left:458px">
    <div class="post-img" role="img" aria-label="Photo of a developer with headphones at a code screen"><div class="post-date"><b>25</b><span>Jul, 2020</span></div></div>
    <h4>Lorem Ipsum is simply dummy text of the printing</h4>
    <p>Lorem Ipsum is simply dummy text of the printing and typesetting industry. Lorem Ipsum has been the industry's.</p>
    <svg width="30" height="14" viewBox="0 0 30 14"><path d="M0 7h28M22 1l6 6-6 6" fill="none" stroke="#222" stroke-width="2"/></svg>
  </article>
  <article class="post" style="left:764px">
    <div class="post-img" role="img" aria-label="Photo of a laptop showing code"><div class="post-date"><b>25</b><span>Jul, 2020</span></div></div>
    <h4>Lorem Ipsum is simply dummy text of the printing</h4>
    <p>Lorem Ipsum is simply dummy text of the printing and typesetting industry. Lorem Ipsum has been the industry's.</p>
    <svg width="30" height="14" viewBox="0 0 30 14"><path d="M0 7h28M22 1l6 6-6 6" fill="none" stroke="#222" stroke-width="2"/></svg>
  </article>
</section>

<div class="contact-band"></div>
<section class="abs contact-card">
  <h2 class="abs heading enquiry-title">ENQUERY ABOUT SERVICES</h2>
  <div class="field" style="top:126px">Name</div>
  <div class="field" style="top:178px">Email</div>
  <div class="field" style="top:231px">Phone</div>
  <div class="field" style="top:277px;height:73px">Message</div>
  <div class="btn btn-send">Send message</div>

  <div class="abs info">
    <h2 class="abs heading info-title">CONTACT INFO</h2>
    <div class="info-item" style="top:120px">
      <svg width="34" height="40" viewBox="0 0 34 40"><path d="M17 2a13 13 0 0 0-13 13c0 11 13 23 13 23s13-12 13-23A13 13 0 0 0 17 2z" fill="none" stroke="#fff" stroke-width="2"/><circle cx="17" cy="15" r="5" fill="none" stroke="#fff" stroke-width="2"/></svg>
      <div><small>Address</small><b>12 Rue des Tilleuls<br>75011 Paris</b></div>
    </div>
    <div class="info-item" style="top:205px">
      <svg width="40" height="30" viewBox="0 0 40 30"><rect x="1" y="1" width="38" height="28" fill="none" stroke="#fff" stroke-width="2"/><path d="M1 1l19 16L39 1M1 29l14-14M39 29L25 15" fill="none" stroke="#fff" stroke-width="2"/></svg>
      <div><small>Email address</small><b>contact@brightvale.coop</b></div>
    </div>
    <div class="info-item" style="top:273px">
      <svg width="40" height="40" viewBox="0 0 40 40"><circle cx="20" cy="20" r="18" fill="none" stroke="#fff" stroke-width="2"/><path d="M13 11l4 0 2 6-3 2c1 3 3 5 6 6l2-3 6 2v4c-9 1-18-8-17-17z" fill="none" stroke="#fff" stroke-width="2"/></svg>
      <div><small>Phone number</small><b>01 47 20 65 18</b></div>
    </div>
    <div class="btn btn-map">View online map</div>
  </div>
</section>

<footer>
  <div class="abs social"><i></i><i></i><i></i><i></i></div>
  <p class="abs copyright">© 2020 Brightvale.coop. All rights reserved</p>
</footer>

</body>
</html>
```